Re-design a website for a millionaire mentor

We need an expert website designer to re-design the website vKeenstride.net

The website would have 4 pages. A home page, Summit Circle page, Hire RM page and an About page.

Here are some reference websites

https://www.lumovance.net
https://rolfbanter.net/

I will also attach a beginning of mockup of the home page I did myself to give an idea of the style we like, please use the quote "If you are not chasing your potential you are wasting your life" instead of the one in the current website...

You don't have the use the mockup (just the quote) and are free to use all your creativity.

Target Market(s)

Entrepreneurs

Number of Pages Required

4 page

Font styles to use
Other font styles liked:
• Franklin Gothic

Requirements
Must have
• -Call of action on the main page to download a free business plan
• -Hire rm page check out reference: http://www.hiremarkbellow.net
• -summit circle page with a button to sign in or join the summit circle. Check out reference for example: https://www.lumovance.net/glide_academy

```html
<!DOCTYPE html>
<html lang="en">
<head>
<meta charset="utf-8">
<title>vKeenstride — Home</title>
<link rel="stylesheet" href="https://fonts.googleapis.com/css2?family=Open+Sans:wght@400;600;700;800&family=Libre+Franklin:wght@600;700;800&display=swap">
<style>
:root{
  --red:#e3262d;
  --ink:#151515;
  --text:#444;
  --white:#fff;
  --footer:#222;
}
*{box-sizing:border-box;margin:0;padding:0}
html,body{width:1200px;height:4500px;overflow:hidden;background:var(--white)}
body{position:relative;font-family:"Open Sans",Arial,sans-serif;color:var(--text)}
.abs{position:absolute}
.photo{position:absolute;background:linear-gradient(135deg,#5a5a5a,#2b2b2b)}
.photo.warm{background:linear-gradient(135deg,#a89a88,#4a4038)}
.photo.city{background:linear-gradient(160deg,#9fb0c2,#4d5a66)}
.photo.light{background:linear-gradient(135deg,#d9d9d9,#8e8e8e)}
.photo.street{background:linear-gradient(135deg,#c7664a,#40506a)}
.heading{font-family:"Libre Franklin","Open Sans",sans-serif;color:var(--ink);font-weight:700}
.link-more{font-size:14px;color:var(--red);font-weight:600;display:flex;align-items:center;gap:10px}
.accent{color:var(--red);font-weight:600}

/* hero */
.hero{left:0;top:0;width:1200px;height:625px;background:var(--red)}
.hero-inner{position:absolute;left:10px;top:10px;width:1180px;height:600px;background:linear-gradient(90deg,#0b0b0b 0%,#1d1d1d 55%,#2c2c2c 100%);overflow:hidden}
.hero-photo{position:absolute;left:640px;top:0;width:540px;height:600px;background:radial-gradient(ellipse at 55% 45%,#4a4a4a 0%,#222 55%,#111 100%)}
.logo{position:absolute;left:150px;top:35px;display:flex;align-items:center;gap:10px;color:var(--white);font-family:"Libre Franklin",sans-serif;font-weight:800;font-size:24px}
.logo .mark{width:26px;height:26px;background:var(--red)}
.nav{position:absolute;right:150px;top:48px;display:flex;gap:30px;font-size:14px;font-weight:600;color:var(--white)}
.nav .active{color:var(--red)}
.hero-title{position:absolute;left:150px;top:262px;color:var(--white);font-family:"Libre Franklin",sans-serif;font-weight:700;font-size:30px;line-height:46px}
.hero-title .hot{color:var(--red);text-transform:uppercase;font-weight:700}
.btn-red{position:absolute;left:150px;top:390px;width:195px;height:52px;background:var(--red);color:var(--white);font-weight:700;font-size:16px;display:flex;align-items:center;justify-content:center;border-radius:3px}
.hero-note{position:absolute;left:155px;top:468px;color:var(--white);font-family:"Open Sans",sans-serif;font-weight:700;font-size:13px}

/* passions */
.passions-title{left:0;top:715px;width:1200px;text-align:center;font-size:30px;font-weight:700;color:var(--ink);letter-spacing:.5px}
.passions-body{left:215px;top:785px;width:770px;text-align:center;font-size:13.5px;line-height:28px}
.dots-right{left:1040px;top:730px;width:160px;height:260px;background:radial-gradient(circle at 100% 50%,rgba(227,38,45,.45),rgba(227,38,45,0) 70%)}

/* summit circle */
.sc-photo{left:0;top:1070px;width:360px;height:265px}
.sc-video{left:230px;top:1140px;width:390px;height:320px;background:var(--red);padding:12px}
.sc-video .photo{position:relative;width:100%;height:100%;background:linear-gradient(135deg,#cfcfcf,#6f6f6f)}
.play{left:402px;top:1278px}
.sc-text{left:685px;top:1145px;width:360px}
.sc-text h2{font-size:34px;margin-bottom:18px}
.sc-text p{font-size:13px;line-height:27px;margin-bottom:20px}

/* academy */
.ac-text{left:160px;top:1670px;width:410px}
.ac-text h2{font-size:34px;margin-bottom:24px}
.ac-text p{font-size:13px;line-height:27px;margin-bottom:20px}
.ac-shadow{left:665px;top:1660px;width:380px;height:360px;background:var(--red)}
.ac-photo{left:645px;top:1635px;width:380px;height:360px}

/* stats */
.stat{top:2115px;width:215px;height:112px;background:var(--white);box-shadow:0 6px 24px rgba(0,0,0,.1);text-align:center;padding-top:25px}
.stat b{display:block;font-size:34px;color:var(--ink);font-weight:600}
.stat span{font-size:12px;color:var(--ink);letter-spacing:.5px}
.stat.hl{border:1.5px solid var(--red)}
.stat.hl b{color:var(--red)}

/* join */
.join-bg{left:0;top:2360px}
.join-text{left:130px;top:2610px;width:370px;text-align:center;color:var(--white)}
.join-text h3{font-size:26px;font-weight:700}
.join-text p{font-size:13px;margin-top:6px;white-space:nowrap}
.join-text .big{font-size:18px;font-weight:700;margin-top:4px}
.btn-dark{display:inline-block;margin-top:28px;background:var(--ink);color:var(--white);font-size:13px;font-weight:600;padding:13px 32px;border-radius:24px}
.sphere{left:840px;top:2390px;width:340px;height:440px;background:radial-gradient(circle,rgba(120,120,120,.28),rgba(120,120,120,0) 68%)}
.quote{width:255px;background:var(--white);box-shadow:0 6px 24px rgba(0,0,0,.12);padding:22px 25px;font-size:13px;line-height:22px;color:var(--text)}
.quote .who{display:flex;align-items:center;gap:14px;margin-top:18px;font-size:12px;color:var(--ink)}
.quote .avatar{width:36px;height:36px;border-radius:50%;background:linear-gradient(135deg,#8a7566,#3b332d)}

/* blog */
.blog-title{left:0;top:3068px;width:1200px;text-align:center;font-size:32px;font-weight:600;color:var(--ink)}
.post{width:265px;background:var(--white);box-shadow:0 6px 24px rgba(0,0,0,.1)}
.post .photo{position:relative;width:100%;height:158px}
.post .body{padding:22px 22px 28px}
.post h4{font-size:15px;color:var(--ink);margin-bottom:12px}
.post p{font-size:13px;line-height:22px;margin-bottom:18px}
.view-all{left:0;top:3618px;width:1200px;text-align:center;color:var(--red);font-size:14px;font-weight:600}

/* follow */
.follow-box{left:405px;top:3860px;width:385px;height:140px;background:var(--red);color:var(--white);font-weight:700;font-size:22px;display:flex;align-items:center;justify-content:center}

/* footer */
.footer{left:0;top:4180px;width:1200px;height:320px;background:var(--footer);color:#cfcfcf;font-size:13px}
.footer .logo{left:165px;top:30px}
.foot-about{position:absolute;left:165px;top:90px;width:190px;line-height:21px;font-size:12px}
.foot-col{position:absolute;top:40px}
.foot-col h5{color:var(--white);font-size:15px;font-weight:600;margin-bottom:16px}
.foot-col li{list-style:none;line-height:22px}
.social li{display:flex;align-items:center;gap:12px;line-height:30px}
.social .dot{width:14px;height:14px;border-radius:50%;background:var(--white)}
.foot-bottom{position:absolute;left:165px;top:275px;width:870px;display:flex;justify-content:space-between;font-size:12px}
.foot-rule{position:absolute;left:0;top:255px;width:1200px;height:1px;background:#333}
</style>
</head>
<body>

<section class="abs hero">
  <div class="hero-inner">
    <div class="hero-photo" role="img" aria-label="Speaker in a dark suit holding a microphone on stage"></div>
    <div class="logo"><span class="mark"></span>vKeenstride</div>
    <nav class="nav"><span>Home</span><span class="active">Summit Circle</span><span>Hire RM</span><span>About</span></nav>
    <h1 class="hero-title">If you are not chasing your <span class="hot">potential</span><br>you are <span class="hot">wasting</span> your life</h1>
    <div class="btn-red" style="left:140px;top:385px">Download Now</div>
    <div class="hero-note" style="left:145px;top:462px">Download My Free Business Plan</div>
  </div>
</section>

<h2 class="abs passions-title">MAKE MONEY BY MONETIZING YOUR PASSIONS!</h2>
<p class="abs passions-body">The answer for entrepreneurs, delivering <span class="accent">VISION, CLARITY and CREATIVE SOLUTIONS</span> to business ideas that have lost their sense of direction. vKeenstride is the pit stop, having the ability to redefine purpose and give new life to an existing set of skills. The objective is to inspire business leaders to take off, confident at full speed, with a new outlook on their business model and products. It is then that the acts of passion, focus, creativity and delivery will launch them to their desired level of success. vKeenstride believes that ANYbody with the right mindset can see, design and live an amazing life!</p>
<div class="abs dots-right" role="img" aria-label="Decorative red dot pattern"></div>

<div class="photo sc-photo" role="img" aria-label="Speaker presenting to an audience"></div>
<div class="abs sc-video"><div class="photo" role="img" aria-label="Video still of mentor in a suit"></div></div>
<svg class="abs play" width="48" height="48" viewBox="0 0 48 48" aria-hidden="true"><circle cx="24" cy="24" r="22" fill="none" stroke="#fff" stroke-width="2.5"/><path d="M19 15 L34 24 L19 33 Z" fill="#fff"/></svg>
<div class="abs sc-text">
  <h2 class="heading">The Summit Circle</h2>
  <p>This program teaches people how to use their time efficiently to help them become the best version of themselves. We’ve created a <span class="accent">summit system</span> that combines high performance coaching techniques, state of the art <span class="accent">productivity principles</span>, and the tools necessary to push your agenda forward and stay on track. The summit circle takes a unique approach to equipping you with <span class="accent">the step-by-step training</span> you’ll need to make more money AND create a life without limits.</p>
  <div class="link-more">Read More <svg width="22" height="10" viewBox="0 0 22 10"><path d="M0 5H20M15 1L20 5L15 9" stroke="#e3262d" stroke-width="1.6" fill="none"/></svg></div>
</div>

<div class="abs ac-text">
  <h2 class="heading">Lift Off Academy</h2>
  <p>Metro Ledger Best Selling Author, Dana Whitlow, and I have partnered up to bring you the one-stop-shop to learning <span class="accent">how to get noticed</span>, promoted, and becoming indispensable at work. In this course you’ll learn the 5 steps to <span class="accent">grow your business</span> and maximize profits, how to advance your career so that you can <span class="accent">increase your salary</span> and receive the income you deserve, how to create passive income (or make money in your sleep), and how to publish and market your first best seller.</p>
  <div class="link-more">Read More <svg width="22" height="10" viewBox="0 0 22 10"><path d="M0 5H20M15 1L20 5L15 9" stroke="#e3262d" stroke-width="1.6" fill="none"/></svg></div>
</div>
<div class="abs ac-shadow"></div>
<div class="photo ac-photo" role="img" aria-label="Mentor presenting in front of a projected slide"></div>

<div class="abs stat" style="left:200px"><b>200</b><span>HAPPY CLIENTS</span></div>
<div class="abs stat hl" style="left:490px"><b>140K</b><span>SUBSCRIBERS</span></div>
<div class="abs stat" style="left:775px"><b>3,800</b><span>USERS</span></div>

<svg class="abs join-bg" width="1200" height="620" viewBox="0 0 1200 620" aria-hidden="true">
  <polygon points="0,0 160,0 600,150 600,430 0,620" fill="#e3262d"/>
</svg>
<div class="abs sphere" role="img" aria-label="Decorative dotted globe pattern"></div>
<div class="abs join-text">
  <h3>JOIN OVER 4,000 PEOPLE</h3>
  <p>We’ve used our business plan to go from overwhelmed</p>
  <div class="big">CLEAR AND PROFITABLE</div>
  <span class="btn-dark">Contact Us</span>
</div>
<div class="abs quote" style="left:520px;top:2500px">You grow with it, and features you didn’t know would be useful are ready when you are.<div class="who"><span class="avatar" role="img" aria-label="Client portrait"></span>Niko Brenn</div></div>
<div class="abs quote" style="left:785px;top:2390px">I am very grateful with it, and features you didn’t know would be useful are ready when you are.<div class="who"><span class="avatar" role="img" aria-label="Client portrait"></span>Nadia</div></div>
<div class="abs quote" style="left:785px;top:2640px">I am very grateful with it, and features you didn’t know would be useful are ready when you are.<div class="who"><span class="avatar" role="img" aria-label="Client portrait"></span>Jonah Waller</div></div>
<div class="abs quote" style="left:495px;top:2735px">I am very grateful with it, and features you didn’t know would be useful are ready when you are.<div class="who"><span class="avatar" role="img" aria-label="Client portrait"></span>Sela Harmon</div></div>

<h2 class="abs blog-title">Blog Post</h2>
<article class="abs post" style="left:160px;top:3160px">
  <div class="photo" role="img" aria-label="Chess pieces on a board"></div>
  <div class="body"><h4>It’s Not About You</h4><p>Your brand is what other people say about you when you’re not in the room, so getting it right is key. When somebody sees your logo, or social media...</p><div class="link-more">Read More <svg width="22" height="10" viewBox="0 0 22 10"><path d="M0 5H20M15 1L20 5L15 9" stroke="#e3262d" stroke-width="1.6" fill="none"/></svg></div></div>
</article>
<article class="abs post" style="left:467px;top:3200px">
  <div class="photo street" role="img" aria-label="Light trails on a city road at night"></div>
  <div class="body"><h4>It’s Not About You</h4><p>Your brand is what other people say about you when you’re not in the room, so getting it right is key. When somebody sees your logo, or social media...</p><div class="link-more">Read More <svg width="22" height="10" viewBox="0 0 22 10"><path d="M0 5H20M15 1L20 5L15 9" stroke="#e3262d" stroke-width="1.6" fill="none"/></svg></div></div>
</article>
<article class="abs post" style="left:775px;top:3160px">
  <div class="photo warm" role="img" aria-label="A word written in sand"></div>
  <div class="body"><h4>It’s Not About You</h4><p>Your brand is what other people say about you when you’re not in the room, so getting it right is key. When somebody sees your logo, or social media...</p><div class="link-more">Read More <svg width="22" height="10" viewBox="0 0 22 10"><path d="M0 5H20M15 1L20 5L15 9" stroke="#e3262d" stroke-width="1.6" fill="none"/></svg></div></div>
</article>
<div class="abs view-all">View All</div>

<div class="photo light" style="left:0;top:3680px;width:310px;height:245px" role="img" aria-label="Mentor speaking on stage"></div>
<div class="photo city" style="left:322px;top:3680px;width:273px;height:245px" role="img" aria-label="Mentor in front of city towers"></div>
<div class="photo street" style="left:605px;top:3680px;width:285px;height:245px" role="img" aria-label="Mentor by a painted mural wall"></div>
<div class="photo" style="left:900px;top:3680px;width:300px;height:245px" role="img" aria-label="Mentor speaking with microphone"></div>
<div class="photo warm" style="left:0;top:3935px;width:280px;height:235px" role="img" aria-label="Mentor seated portrait"></div>
<div class="photo city" style="left:290px;top:3935px;width:300px;height:235px" role="img" aria-label="Rooftop city view"></div>
<div class="photo light" style="left:600px;top:3935px;width:300px;height:235px" role="img" aria-label="Mentor walking through a hall"></div>
<div class="photo warm" style="left:910px;top:3935px;width:290px;height:235px" role="img" aria-label="Mentor with event guests"></div>
<div class="abs follow-box">Follow Us On Snapwall</div>

<footer class="abs footer">
  <div class="logo"><span class="mark"></span>vKeenstride</div>
  <p class="foot-about">The answer for entrepreneurs, delivering VISION, CLARITY and CREATIVE SOLUTIONS to business ideas that have lost their sense of direction.</p>
  <div class="foot-col" style="left:410px"><h5>Quick Links</h5><ul><li>Home</li><li>About</li><li>Summit Circle</li><li>Hire RM</li><li>Contact</li></ul></div>
  <div class="foot-col" style="left:590px"><h5>Contact</h5><ul><li>418 Orchard Lane, Suite 12</li><li>Brookvale, OH 44012</li><li style="margin-top:14px;color:#fff;font-weight:600">(555) 014-2290</li></ul></div>
  <div class="foot-col social" style="left:815px"><h5>Follow US</h5><ul><li><span class="dot"></span>Friendly</li><li><span class="dot"></span>Chatter</li><li><span class="dot"></span>Circles</li><li><span class="dot"></span>Vidstream</li></ul></div>
  <div class="foot-rule"></div>
  <div class="foot-bottom"><span>Copyright © 2019 - vKeenstride</span><span>Privacy Policy | Disclaimer | Refund Policy</span></div>
</footer>

</body>
</html>
```